Agriculture Technology Website Design Project

We need a new website for a company called Brook Ledger Works. We have a document laid out with all of the requirements (see below) and would like you to follow the instructions on there. In this document, there is all of the copy that must be included on the website and what order it should go in as well as images. These images have specific names and are listed in the document as to where they should go. Please make this one continuous site that users can easily scroll through. We would like it to be sleek and modern with as little clutter as possible. Please refer to the brochure that we have posted below (Stone Analytica.pdf) for a design we have had done for the company in the past. We really like this design and it would be great if the color scheme was similar on the website.

Industry/Entity Type

Agriculture

Number of Pages Required

1 page

Font styles to use
Sans Serif

```html
<!DOCTYPE html>
<html lang="en">
<head>
<meta charset="utf-8">
<title>Brook Ledger Works</title>
<link href="https://fonts.googleapis.com/css2?family=Montserrat:wght@300;400;500;600;700&family=Poppins:wght@300;400;500;600&display=swap" rel="stylesheet">
<style>
:root{
  --green:#2f7a2f;
  --green-dark:#25632a;
  --ink:#222222;
  --text:#777777;
  --dark:#262626;
  --darker:#1c1c1c;
  --light:#f4f4f4;
  --white:#ffffff;
}
*{margin:0;padding:0;box-sizing:border-box}
html,body{width:1200px;height:4144px;overflow:hidden}
body{font-family:'Poppins',sans-serif;color:var(--text);background:var(--white);font-size:10px;line-height:1.6}
.section{position:relative;width:1200px;overflow:hidden}
.abs{position:absolute}
h1,h2,h3,h4,.heading{font-family:'Montserrat',sans-serif;color:var(--ink);font-weight:500}
.eyebrow{font-family:'Montserrat',sans-serif;font-size:9px;font-weight:600;color:var(--green);text-transform:uppercase;letter-spacing:.3px}
.rule{width:34px;height:2px;background:linear-gradient(90deg,var(--green) 0 16px,transparent 16px 20px,var(--green) 20px 26px,transparent 26px 29px,var(--green) 29px)}
.btn{display:flex;align-items:center;justify-content:center;background:var(--green);color:var(--white);font-family:'Montserrat',sans-serif;font-weight:600;font-size:9px;text-transform:uppercase}
.btn-case{text-transform:none}
.photo{background:linear-gradient(160deg,#8fa07d,#5f6d48 60%,#3f4a33)}

/* top bar */
.topbar{height:29px;border-bottom:1px solid #ececec;font-size:8px;color:#888}
.social-dot{width:7px;height:7px;border-radius:50%;background:#888}
/* header */
.header{height:76px}
.brand{font-family:'Montserrat',sans-serif;font-weight:600;font-size:12px;color:var(--green);display:flex;align-items:center;gap:8px;line-height:1.15}
.brand-mark{width:22px;height:22px;border-radius:50%;background:var(--green)}
.contact-item{display:flex;align-items:center;gap:10px}
.contact-item b{display:block;font-family:'Montserrat',sans-serif;font-weight:600;font-size:10px;color:var(--ink)}
.contact-item span{font-size:8.5px;color:#999}
/* nav */
.nav{height:40px;background:var(--dark)}
.nav a{position:absolute;top:13px;font-family:'Montserrat',sans-serif;font-weight:600;font-size:9px;color:var(--white);text-decoration:none}
.nav a.active{color:#6fb24a}
/* hero */
.hero{height:440px;background:linear-gradient(180deg,#5a6a78 0%,#7b8a86 35%,#6c6f5d 60%,#4c4a40 100%)}
.hero-title{font-size:52px;color:var(--white);font-weight:500;text-align:center;width:1200px;top:160px}
.hero-sub{color:#eee;font-size:11px;text-align:center;width:1200px;top:225px}
/* about */
.about{height:488px;background:linear-gradient(180deg,#fff 55%,#f1f1f1)}
.about p{font-size:9px;line-height:1.75;color:#888;width:330px}
/* stats */
.stats{height:106px}
.stat-card{position:absolute;top:21px;width:213px;height:64px;background:var(--white);display:flex;align-items:center;gap:10px;padding-left:10px}
.stat-card h4{font-size:12px;font-weight:500}
.stat-card span{font-size:8.5px;color:#777}
.icon-circle{width:34px;height:34px;border:1.5px solid #555;border-radius:50%;flex:none}
/* products */
.products{height:518px;background:var(--light)}
.card{position:absolute;background:var(--white);padding:22px 14px 0 60px}
.card h4{font-size:11.5px;font-weight:500;text-transform:uppercase;line-height:1.4;margin-bottom:6px}
.card p{font-size:8.5px;color:#999;line-height:1.8}
.card .more{font-family:'Montserrat',sans-serif;font-size:8.5px;font-weight:600;color:var(--green);margin-top:6px;display:block}
.card svg{position:absolute;left:16px;top:24px}
/* why */
.why p{font-size:9px;color:#ddd;width:300px}
/* projects */
.projects{height:568px}
.cell{position:absolute;width:230px;height:180px}
/* testimonial */
.testi{height:344px}
.testi-list li{list-style:none;font-size:9px;color:#eaf3e3;display:flex;align-items:center;gap:8px;margin-bottom:4px}
.tick{width:9px;height:9px;border-radius:50%;background:#fff;flex:none}
/* team */
.team{height:480px}
.member-label{position:absolute;width:201px;height:56px;background:var(--white);border-top:3px solid var(--green);border-left:3px solid var(--green);box-shadow:0 4px 14px rgba(0,0,0,.08);text-align:center;padding-top:10px}
.member-label h4{font-size:12px;font-weight:500}
.member-label span{font-size:8.5px;color:#999}
/* footer */
.footer{height:402px;background:var(--dark);color:#ddd}
.foot-col h4{font-size:12px;color:#fff;font-weight:500;border-left:2px solid #6fb24a;padding-left:8px;margin-bottom:18px}
.foot-col p,.foot-col li{font-size:8.5px;color:#ddd;list-style:none;line-height:1.75}
.foot-col li{margin-bottom:14px}
.foot-col li::before{content:"+ ";color:#6fb24a}
</style>
</head>
<body>

<!-- top bar -->
<div class="section topbar">
  <span class="abs" style="left:257px;top:8px">Your Trusted 24 Hours Service Provider!</span>
  <span class="abs" style="left:745px;top:8px">Office Hour : 08:00am - 6:00pm</span>
  <div class="abs" style="left:888px;top:11px;display:flex;gap:9px"><i class="social-dot"></i><i class="social-dot"></i><i class="social-dot"></i><i class="social-dot"></i></div>
</div>

<!-- header -->
<header class="section header">
  <div class="brand abs" style="left:245px;top:24px"><i class="brand-mark"></i><span>Brook Ledger<br>Works</span></div>
  <div class="contact-item abs" style="left:487px;top:22px">
    <svg width="22" height="22" viewBox="0 0 24 24" fill="none" stroke="#999" stroke-width="1.3"><path d="M5 3h4l2 5-3 2a12 12 0 0 0 6 6l2-3 5 2v4a2 2 0 0 1-2 2A17 17 0 0 1 3 5a2 2 0 0 1 2-2z"/></svg>
    <div><b>555-014-2286</b><span>Make A Call</span></div>
  </div>
  <div class="contact-item abs" style="left:627px;top:22px">
    <svg width="22" height="22" viewBox="0 0 24 24" fill="none" stroke="#999" stroke-width="1.3"><rect x="2" y="5" width="20" height="14"/><path d="M2 5l10 8 10-8"/></svg>
    <div><b>info@brookledgerworks.com</b><span>Get A Estimate</span></div>
  </div>
  <div class="contact-item abs" style="left:830px;top:22px">
    <svg width="22" height="22" viewBox="0 0 24 24" fill="none" stroke="#999" stroke-width="1.3"><circle cx="12" cy="12" r="10"/><path d="M2 12h20M12 2c3 3 3 17 0 20M12 2c-3 3-3 17 0 20"/></svg>
    <div><b>Newyork USA</b><span>48 Alder Row, Florida</span></div>
  </div>
</header>

<!-- nav -->
<nav class="section nav">
  <a class="active" style="left:257px">ABOUT US</a>
  <a style="left:333px">WHY BLW?</a>
  <a style="left:409px">PRODUCTS</a>
  <a style="left:487px">PARTNERS</a>
  <a style="left:563px">CONTACT US</a>
  <div class="btn abs" style="left:820px;top:0;width:137px;height:40px">Request for quote</div>
</nav>

<!-- hero -->
<section class="section hero" role="img" aria-label="Farm field with irrigation pump equipment and orchard trees under a cloudy sky">
  <h1 class="hero-title abs">Brook Ledger Works</h1>
  <p class="hero-sub abs">Bringing industrial automation to the farm</p>
  <div class="btn abs" style="left:544px;top:283px;width:112px;height:30px">More About</div>
</section>

<!-- about -->
<section class="section about">
  <div class="abs" style="left:548px;top:0;width:409px;height:8px;background:var(--green)"></div>
  <div class="abs" style="left:238px;top:55px;width:343px;height:340px;background:#fff;box-shadow:0 6px 20px rgba(0,0,0,.08)"></div>
  <div class="photo abs" style="left:265px;top:57px;width:316px;height:333px;background:linear-gradient(180deg,#9fb6cf 0%,#c9c7b3 30%,#6f7d45 55%,#4b5b2c 100%)" role="img" aria-label="Farmer walking between rows of young crops"></div>
  <svg class="abs" style="left:411px;top:200px" width="42" height="42" viewBox="0 0 42 42"><circle cx="21" cy="21" r="19" fill="none" stroke="#fff" stroke-width="2"/><path d="M17 13l11 8-11 8z" fill="none" stroke="#fff" stroke-width="2"/></svg>
  <div class="abs" style="left:621px;top:60px">
    <div class="eyebrow">About</div>
    <h2 style="font-size:21px;margin:2px 0 10px">BLW is a Systems Integrator</h2>
    <div class="rule" style="margin-bottom:14px"></div>
    <p>Our focus is on helping California growers design, build and adopt effective irrigation management solutions.</p>
    <p style="margin-top:9px">Our team has worked together for over 15 years, providing monitoring and control systems for 60+ crops that have successfully helped over 500 farms significantly improve irrigation management.</p>
    <p style="margin-top:9px">We also farm our own 200 acre technology lab to help ensure we deliver reliable monitoring and automation to your farm.</p>
    <h2 style="font-size:24px;margin:14px 0 10px">OUR GOAL</h2>
    <p>to be your trusted partner for technology adoption</p>
    <div class="btn btn-case" style="width:103px;height:29px;margin-top:14px">Our Products</div>
  </div>
</section>

<!-- stats -->
<section class="section stats" style="height:106px;margin-top:0;background:#f1f1f1">
  <div class="abs" style="left:245px;top:0;width:712px;height:106px;background:var(--green)"></div>
  <div class="stat-card" style="left:262px"><i class="icon-circle"></i><div><h4>25 Years Of Experiance</h4><span>All about planting and growing.</span></div></div>
  <div class="stat-card" style="left:494px"><i class="icon-circle" style="border-radius:4px"></i><div><h4>Experianced Workers</h4><span>All about planting and growing.</span></div></div>
  <div class="stat-card" style="left:725px"><svg width="34" height="34" viewBox="0 0 34 34" fill="none" stroke="#555" stroke-width="1.5"><path d="M6 5h22v8a11 11 0 0 1-22 0z"/><path d="M17 24v5M11 30h12"/></svg><div><h4>100+ Awards Win</h4><span>All about planting and growing.</span></div></div>
</section>

<!-- agriculture -->
<section class="section" style="height:298px;background:linear-gradient(180deg,#fafafa,#fff)">
  <svg class="abs" style="left:584px;top:62px" width="32" height="36" viewBox="0 0 32 36" fill="none" stroke="var(--green)" stroke-width="1.4"><path d="M4 12h24M9 12l3-8h8l3 8"/><circle cx="16" cy="18" r="5"/><path d="M5 35c1-7 5-10 11-10s10 3 11 10"/></svg>
  <div class="eyebrow abs" style="width:1200px;text-align:center;top:102px">About Agriculture</div>
  <h2 class="abs" style="width:1200px;text-align:center;top:122px;font-size:27px;font-weight:600">Agriculture Is Providing The Best</h2>
  <h2 class="abs" style="width:1200px;text-align:center;top:158px;font-size:27px;font-weight:300">Solution Of Eco Environment</h2>
  <div class="btn btn-case abs" style="left:512px;top:216px;width:69px;height:27px;background:var(--darker)">About</div>
  <div class="btn btn-case abs" style="left:589px;top:216px;width:100px;height:27px">Our Services</div>
</section>

<!-- products -->
<section class="section products">
  <div class="abs" style="left:245px;top:60px;width:220px">
    <div class="eyebrow">What we offer</div>
    <h2 style="font-size:21px;margin:2px 0 10px">Our Products</h2>
    <div class="rule" style="margin-bottom:14px"></div>
    <p style="font-size:8.5px;line-height:1.8;color:#999">We provide marketing services to startups and small businesses to looking for a opment.</p>
    <p style="font-family:Montserrat,sans-serif;font-size:8.5px;font-weight:600;color:var(--ink);margin-top:20px">Learn More ›</p>
  </div>
  <div class="card" style="left:487px;top:59px;width:226px;height:142px">
    <svg width="32" height="32" viewBox="0 0 32 32" fill="none" stroke="var(--green)" stroke-width="1.3"><path d="M4 28h24M8 28V14M8 14c-4 0-5-4-5-6 3 0 5 2 5 6zM8 14c4 0 5-4 5-6-3 0-5 2-5 6M20 28V10"/><circle cx="20" cy="8" r="3"/></svg>
    <h4>Crop Monitoring</h4>
    <p>Ensuring that you have real-time information to optimize irrigation management</p>
    <span class="more">Learn More ›</span>
  </div>
  <div class="card" style="left:732px;top:59px;width:225px;height:142px">
    <svg width="32" height="32" viewBox="0 0 32 32" fill="none" stroke="var(--green)" stroke-width="1.3"><path d="M16 4v8M10 12h12l-2 6h-8zM3 28h26M6 28c0-3 2-5 4-5s4 2 4 5M18 28c0-3 2-5 4-5s4 2 4 5"/></svg>
    <h4>Pump Monitoring<br>And Control</h4>
    <p>Scalable and cost-effective pump monitoring with built-in remote control</p>
    <span class="more">Learn More ›</span>
  </div>
  <div class="card" style="left:487px;top:220px;width:226px;height:140px">
    <svg width="32" height="32" viewBox="0 0 32 32" fill="none" stroke="var(--green)" stroke-width="1.3"><path d="M4 28h24M16 28V16M16 16c-6 0-8-5-8-9 5 0 8 3 8 9zM16 16c6 0 8-5 8-9-5 0-8 3-8 9"/><path d="M4 8l3 3M28 8l-3 3"/></svg>
    <h4>Irrigation<br>Automation</h4>
    <p>Upgrade your irrigation system: from retrofit to ranch-wide automation</p>
    <span class="more">Learn More ›</span>
  </div>
  <div class="card" style="left:732px;top:220px;width:225px;height:140px">
    <svg width="32" height="32" viewBox="0 0 32 32" fill="none" stroke="var(--green)" stroke-width="1.3"><path d="M6 28h20M16 28V14M16 14c-5 0-7-4-7-8 4 0 7 3 7 8zM16 14l8-8M20 6h4v4"/></svg>
    <h4>Control Panel<br>Design And Build</h4>
    <p>Leverage BLW design and build expertise to meet your exact needs and specifications</p>
    <span class="more">Learn More ›</span>
  </div>
  <div class="card" style="left:236px;top:251px;width:226px;height:107px;padding-top:20px">
    <svg width="32" height="32" viewBox="0 0 32 32" fill="none" stroke="var(--green)" stroke-width="1.3" style="top:26px"><path d="M6 26l10-10M16 16c0-6 4-10 10-10 0 6-4 10-10 10zM10 10c-4 0-6 3-6 6 4 0 6-2 6-6"/></svg>
    <h4>Contact Us</h4>
    <p>For immediate support call (555-014-2286)</p>
    <span class="more">Get In Touch ›</span>
  </div>
</section>

<!-- why -->
<section class="section why" style="height:392px">
  <div class="abs" style="left:0;top:24px;width:1200px;height:322px;background:#2b2b2b"></div>
  <div class="abs" style="left:600px;top:0;width:357px;height:370px;background:var(--green)"></div>
  <div class="abs" style="left:1118px;top:24px;width:82px;height:322px;background:#0d0d0d"></div>
  <div class="abs" style="left:624px;top:24px;width:494px;height:322px;background:linear-gradient(180deg,#c9d3d6 0%,#a9b3a4 25%,#6c8a3d 45%,#4e6e2b 100%)" role="img" aria-label="Wide field of young crop rows with hills in the distance"></div>
  <div class="abs" style="left:245px;top:77px">
    <div class="eyebrow" style="color:#6fb24a">Why BLW?</div>
    <h2 style="font-size:21px;color:#fff;line-height:1.3;margin:4px 0 12px;width:300px">We're your local farm data team.</h2>
    <div class="rule" style="margin-bottom:14px"></div>
    <p>We are experts at deploying Information Technology for irrigation management.</p>
    <p style="margin-top:9px">We partner with our customers to deliver the right solutions.</p>
    <p style="margin-top:9px">Everything we sell is off-the-shelf, cost-effective and reliable.</p>
    <div class="btn btn-case" style="width:98px;height:28px;margin-top:20px">Get In Touch</div>
  </div>
</section>

<!-- projects -->
<section class="section projects">
  <div class="eyebrow abs" style="width:1200px;text-align:center;top:58px">Recently Completed</div>
  <h2 class="abs" style="width:1200px;text-align:center;top:76px;font-size:22px">Our Latest Projects</h2>
  <div class="rule abs" style="left:583px;top:110px"></div>
  <div class="abs" style="left:0;top:143px;width:1200px;height:270px;background:#f2f2f2"></div>
  <div class="abs" style="left:241px;top:136px;width:716px;height:382px;background:#fff"></div>
  <div class="cell" style="left:249px;top:143px;background:linear-gradient(180deg,#7b8fa6 0%,#8e8e7c 40%,#bfc6c6 70%,#8a8a85 100%)" role="img" aria-label="Solar powered sensor station in a newly planted field"></div>
  <div class="cell" style="left:484px;top:143px;background:linear-gradient(135deg,#a39276,#cbb65e 45%,#8d7d64)" role="img" aria-label="Cable conduit and yellow tape on bare soil"></div>
  <div class="cell" style="left:719px;top:143px;background:linear-gradient(180deg,#8e8070,#6a6358 50%,#9a8a77)" role="img" aria-label="Sensor mounted on a metal post"></div>
  <div class="cell" style="left:249px;top:330px;background:linear-gradient(180deg,#3a86d0,#6aa7de 60%,#9ec4e8)" role="img" aria-label="Weather station on a pole against blue sky"></div>
  <div class="cell" style="left:484px;top:330px;background:linear-gradient(180deg,#a59a8a,#c8c1b5 50%,#8e8678)" role="img" aria-label="Solar panel and control box in a vineyard row"></div>
  <div class="cell" style="left:719px;top:330px;background:linear-gradient(180deg,#5b8fc4,#3d5c3f 55%,#2e3f36)" role="img" aria-label="Irrigation pumps and valves outdoors"></div>
</section>

<!-- testimonial -->
<section class="section testi">
  <div class="abs" style="left:0;top:0;width:1200px;height:307px;background:linear-gradient(90deg,#2e7b30,#3a8a35 60%,#2d7430)"></div>
  <div class="abs" style="left:245px;top:43px;width:345px;height:301px;background:#2b2b2b;text-align:center;color:#fff">
    <div style="width:51px;height:51px;margin:39px auto 0;background:#7a9a5c;border:2px solid #fff" role="img" aria-label="Portrait of the reviewer"></div>
    <h4 style="color:#fff;font-size:11.5px;margin-top:14px">Evan Rhodes</h4>
    <div style="font-size:7.5px;color:#ccc">Ceo Of Farming</div>
    <p style="font-style:italic;font-size:9px;line-height:1.8;width:300px;margin:18px auto 0;color:#eee">Lorem Ipsum is simply dummy text of the printing and typesetting industry. Lorem Ipsum has been the industry's standard dummy text ever since the 1500s, when an unknown printer took a galley of type and scrambled it to make a type specimen book. Remaining essentially unchanged.</p>
    <div style="display:flex;gap:8px;justify-content:center;margin-top:26px"><i style="width:6px;height:6px;border-radius:50%;background:var(--green)"></i><i style="width:5px;height:5px;border-radius:50%;background:#fff"></i><i style="width:5px;height:5px;border-radius:50%;background:#fff"></i></div>
  </div>
  <div class="abs" style="left:619px;top:47px;width:330px">
    <div class="eyebrow" style="color:#fff">What we offer</div>
    <h2 style="font-size:21px;color:#fff;margin:2px 0 8px">What We Archived</h2>
    <div class="rule" style="margin-bottom:12px;filter:brightness(3)"></div>
    <p style="font-size:9px;color:#eaf3e3;line-height:1.8;margin-bottom:12px">Eco-friendly products are, the products that do not harm the whether. environment in their production.</p>
    <ul class="testi-list">
      <li><i class="tick"></i>Lorem ipsum dolor sit amet, consectetur adipiscing elit.</li>
      <li><i class="tick"></i>Donec vel erat sollicitudin, dapibus dui at, porttitor sem.</li>
      <li><i class="tick"></i>Sed consequat justo in nisl sagittis porta.</li>
    </ul>
    <div class="btn btn-case" style="width:68px;height:26px;margin-top:16px;background:#fff;color:var(--ink)">About</div>
  </div>
</section>

<!-- team -->
<section class="section team" style="margin-top:-38px">
  <div class="abs" style="left:245px;top:100px">
    <div class="eyebrow">Team Member</div>
    <h2 style="font-size:21px;margin-top:2px">Meet Our Great Team</h2>
  </div>
  <p class="abs" style="left:528px;top:104px;width:310px;font-size:8.5px;color:#999;line-height:1.8">Our team mission is to promote agricultural practices designed to provide abundant healthy food, fiber and other services for all communities.</p>
  <div class="btn btn-case abs" style="left:865px;top:95px;width:92px;height:29px;background:#fff;color:var(--ink);border:1.5px solid #555">View More</div>

  <div class="photo abs" style="left:253px;top:161px;width:207px;height:210px;background:linear-gradient(180deg,#7d6a4d,#a88a67 50%,#6a7a49)" role="img" aria-label="Team member portrait in a greenhouse"></div>
  <div class="member-label" style="left:277px;top:359px"><h4>Nora Vell</h4><span>Landscaper</span></div>
  <div class="photo abs" style="left:497px;top:161px;width:206px;height:210px;background:linear-gradient(180deg,#5b5a4c,#8b7a62 50%,#4a4a3e)" role="img" aria-label="Team member portrait in a barn"></div>
  <div class="member-label" style="left:518px;top:359px"><h4>Hal Brenner</h4><span>Gardener</span></div>
  <div class="photo abs" style="left:740px;top:161px;width:206px;height:210px;background:linear-gradient(180deg,#4e4a40,#7c6b55 50%,#3d3a33)" role="img" aria-label="Team member portrait with work gloves"></div>
  <div class="member-label" style="left:762px;top:359px"><h4>Owen Tate</h4><span>Landscaper</span></div>
</section>

<!-- footer -->
<footer class="section footer" style="margin-top:-38px">
  <div class="abs" style="left:0;top:0;width:1200px;height:80px;border-bottom:1px solid #3a3a3a"></div>
  <div class="abs" style="left:531px;top:0;width:137px;height:80px;background:#2f2f2f;text-align:center;padding-top:26px">
    <div style="font-size:8px;color:#6fb24a">Call Us On</div>
    <div style="font-family:Montserrat,sans-serif;font-size:9.5px;font-weight:600;color:#fff">+123 456 789 0000</div>
  </div>
  <div class="abs" style="left:245px;top:30px;display:flex;align-items:center;gap:8px;font-family:Montserrat,sans-serif;font-size:11.5px;color:#fff">
    <svg width="12" height="12" viewBox="0 0 12 12" fill="none" stroke="#fff"><circle cx="6" cy="6" r="5"/><path d="M7 3.5L4.5 6 7 8.5"/></svg>Find Our Nearest Office
    <svg style="margin-left:14px" width="30" height="30" viewBox="0 0 30 30" fill="none" stroke="#6fb24a" stroke-width="1.4"><path d="M3 14L15 4l12 10M6 12v15h18V12M12 27v-8h6v8"/></svg>
  </div>
  <div class="abs" style="left:732px;top:24px;display:flex;align-items:center;gap:14px;font-family:Montserrat,sans-serif;font-size:11.5px;color:#fff">
    <svg width="30" height="30" viewBox="0 0 30 30" fill="none" stroke="#6fb24a" stroke-width="1.4"><circle cx="15" cy="15" r="13"/><path d="M10 15l4 4 7-8"/></svg>Emergency Restorations
    <svg width="12" height="12" viewBox="0 0 12 12" fill="none" stroke="#fff"><circle cx="6" cy="6" r="5"/><path d="M5 3.5L7.5 6 5 8.5"/></svg>
  </div>

  <div class="foot-col abs" style="left:245px;top:117px;width:160px">
    <h4>About</h4>
    <p>Lorem Ipsum is simply dummy text of the printing and typesetting industry. Lorem Ipsum has been the industry's</p>
    <p style="margin-top:14px">standard dummy text ever since the 1500s, when an unknown printer took a galley of type and scrambled it to make a type specimen book.</p>
    <p style="margin-top:18px;font-family:Montserrat,sans-serif;font-size:10px;color:#fff">Find Us On Map ›</p>
  </div>
  <div class="foot-col abs" style="left:426px;top:117px">
    <h4>Useful Links</h4>
    <ul><li>Home</li><li>About Us</li><li>Our Products</li><li>Why BLW?</li><li>Partners</li><li>Contact Us</li></ul>
  </div>
  <div class="foot-col abs" style="left:608px;top:117px">
    <h4>Follow Us</h4>
    <ul><li>Social One</li><li>Social Two</li><li>Social Three</li></ul>
  </div>
  <div class="foot-col abs" style="left:791px;top:117px;width:170px">
    <h4>Get In Touch</h4>
    <div style="display:flex;gap:12px"><svg width="10" height="12" viewBox="0 0 10 12" fill="#fff"><path d="M5 0a4 4 0 0 1 4 4c0 3-4 8-4 8S1 7 1 4a4 4 0 0 1 4-4z"/></svg><p>4789 Harrow Street, Fenwick Mashton Town</p></div>
    <div style="display:flex;gap:12px;margin-top:24px"><svg width="10" height="12" viewBox="0 0 24 24" fill="#fff"><path d="M5 3h4l2 5-3 2a12 12 0 0 0 6 6l2-3 5 2v4a2 2 0 0 1-2 2A17 17 0 0 1 3 5a2 2 0 0 1 2-2z"/></svg><p>555-014-2286</p></div>
    <div style="display:flex;gap:12px;margin-top:24px"><svg width="11" height="10" viewBox="0 0 24 20" fill="none" stroke="#fff" stroke-width="2"><rect x="1" y="2" width="22" height="16"/><path d="M1 2l11 9 11-9"/></svg><p>info@brookledgerworks.com</p></div>
  </div>

  <p class="abs" style="width:1200px;text-align:center;top:372px;font-size:8.5px;color:#ddd">Copyright @ 2020 <b style="color:#fff">www.brookledgerworks.com</b></p>
  <div class="abs" style="left:1155px;top:345px;width:23px;height:23px;background:var(--green);display:flex;align-items:center;justify-content:center">
    <svg width="10" height="8" viewBox="0 0 10 8" fill="none" stroke="#fff" stroke-width="1.5"><path d="M1 6l4-4 4 4"/></svg>
  </div>
</footer>

</body>
</html>
```